New DL Brochures for Kites Gymnastics Centres

Kites Gymnastics is about to launch its new website and to coincide with this we would like to produce a complete new set of brochures for all of our programs (10 programs)
Kites Gymnastics provides sports coaching for young children in gymnastics lessons as well as conducting holiday programs and birthday parties.
Our company colours are red, gold and black but we are trying to maintain a clean, sharp image so lots of white should be used to highlight our colours.
The brochures should all follow the same template and be clean, fresh, simple and exciting making you want to use our services.
Each brochure should contain 1 or 2 pictures (you decide !) as well as our logo (ideally at the top) with our contact details at the bottom (contact details will be required to be changed for each of our 4 locations)
We have a supply of images which will replace the stock photo supplied for the winning bid.
UPDATE - I will consider postcard type designs which may allow a more diverse range of ideas - this could be very effective way to display the information
Updates
Project Deadline Extended
Reason: I have increased the budget and would like to encourage more designs :)
I am now considering postcard type designs for this project as well as DL sized designs. After looking over a couple of designs it may be possible to do a great "postcard" style design with a great picture and basic info on the front and program info on the back of the postcard
Hi All,
Target Market(s)
Parents of young children
Industry/Entity Type
It Company
Look and feel
Each slider illustrates characteristics of the customer's brand and the style your logo design should communicate.

```html
<!DOCTYPE html>
<html lang="en">
<head>
<meta charset="utf-8">
<title>Kites Gymnastics – Mini Kites</title>
<link href="https://fonts.googleapis.com/css2?family=Archivo+Narrow:wght@400;700&family=Oswald:wght@500;600&display=swap" rel="stylesheet">
<style>
  :root {
    --red: #d7282f;
    --red-dark: #c21f26;
    --gold: #e4ad3b;
    --gold-light: #f7df9f;
    --ink: #231f20;
    --white: #ffffff;
    --pattern-pink: #f2a7ab;
  }
  * { margin: 0; padding: 0; box-sizing: border-box; }
  html, body { width: 1200px; height: 2545px; overflow: hidden; background: var(--white); }
  .brochure { position: relative; width: 1200px; height: 2545px; background: var(--white); font-family: "Archivo Narrow", sans-serif; }
  .header-band { position: absolute; top: 0; left: 0; width: 1200px; height: 560px; }
  .brand-name {
    position: absolute; left: 94px; top: 170px;
    font-family: "Oswald", sans-serif;
    color: var(--red); line-height: 1; text-transform: uppercase;
  }
  .brand-name .line-1 { display: block; font-size: 92px; font-weight: 600; letter-spacing: 2px; }
  .brand-name .line-2 { display: block; font-size: 92px; font-weight: 600; letter-spacing: 4px; margin-top: -6px; }
  .pattern {
    position: absolute; left: 60px; top: 560px; width: 1080px; height: 880px;
    background: radial-gradient(ellipse at 50% 50%, rgba(255,255,255,1) 0 9%, rgba(242,167,171,0.55) 24%, rgba(242,167,171,0.28) 46%, rgba(255,255,255,0) 70%);
  }
  .program-title {
    position: absolute; left: 0; top: 1190px; width: 1200px; text-align: center;
    color: var(--red); font-size: 80px; line-height: 1; font-weight: 400;
    text-decoration: underline; text-decoration-thickness: 3px; text-underline-offset: 8px;
  }
  .age-range { position: absolute; left: 0; top: 1300px; width: 1200px; text-align: center; font-size: 32px; color: var(--ink); }
  .photo {
    position: absolute; left: 215px; top: 1370px; width: 770px; height: 700px;
    background: linear-gradient(160deg, #f3ede6 0%, #b98a5e 45%, #8c5a36 75%, #c9433c 100%);
  }
  .offer-box {
    position: absolute; left: 94px; top: 2092px; width: 1012px; height: 160px;
    border: 4px solid var(--red); border-radius: 18px;
    display: flex; flex-direction: column; justify-content: center; align-items: center;
    color: var(--red-dark); font-size: 44px; line-height: 1.25;
  }
  .contact-footer {
    position: absolute; left: 0; bottom: 0; width: 1200px; height: 184px; background: var(--red);
    color: var(--white); text-align: center; font-size: 26px; line-height: 1.25; padding-top: 28px; font-weight: 700;
  }
</style>
</head>
<body>
<div class="brochure">
  <svg class="header-band" viewBox="0 0 1200 560" aria-hidden="true">
    <defs>
      <linearGradient id="goldFade" x1="0" y1="0" x2="1" y2="0">
        <stop offset="0" stop-color="#e4ad3b"/>
        <stop offset="1" stop-color="#f7df9f"/>
      </linearGradient>
    </defs>
    <polygon points="0,0 1200,0 1200,345 0,550" fill="url(#goldFade)"/>
  </svg>

  <div class="brand-name">
    <span class="line-1">Kites</span>
    <span class="line-2">Gymnastics</span>
  </div>

  <div class="pattern" role="img" aria-label="Decorative swirl of pink dots radiating from the centre"></div>

  <h1 class="program-title">MINI KITES</h1>
  <p class="age-range">(2-5 years)</p>

  <div class="photo" role="img" aria-label="Photo of a coach helping a young child climb on a wooden gym frame"></div>

  <div class="offer-box">
    <p>Give your child the best start in life</p>
    <p>Book NOW for a Free Mini Kites Try Out Class</p>
  </div>

  <footer class="contact-footer">
    <p>Address</p>
    <p>Lorem ipsum dolor sit amet,</p>
    <p>consectetuer adipiscing elit,</p>
  </footer>
</div>
</body>
</html>
```